Painting Company Business Card

Brightwell Painting needs a new business card. See attachments for our logo and current card as an example.
We want to utilize the same colors in the logo, and keep all the information that is currently on it. Just need an updated and modern design.
We are open to loosing the Association Logos if it means a better design.
We are also entertaining a spot for a picture of a headshot of the person listed on the card. Head shot can be finished later.

```html
<!DOCTYPE html>
<html lang="en">
<head>
<meta charset="utf-8">
<title>Brightwell Painting — Business Card</title>
<link href="https://fonts.googleapis.com/css2?family=Lato:wght@400;700;900&display=swap" rel="stylesheet">
<style>
  :root {
    --backdrop: #e9e4dc;
    --kraft-light: #d7b78c;
    --kraft-mid: #c49a68;
    --kraft-dark: #b3834f;
    --ink: #111111;
    --card-shadow: rgba(0, 0, 0, 0.35);
  }
  * { margin: 0; padding: 0; box-sizing: border-box; }
  html, body {
    width: 1200px;
    height: 900px;
    overflow: hidden;
    background: var(--backdrop);
    font-family: "Lato", sans-serif;
    color: var(--ink);
  }
  .stage {
    position: relative;
    width: 1200px;
    height: 900px;
  }
  .card {
    position: absolute;
    left: 330px;
    width: 556px;
    height: 342px;
    background: radial-gradient(ellipse at 45% 20%, var(--kraft-light) 0%, var(--kraft-mid) 55%, var(--kraft-dark) 100%);
    box-shadow: 2px 4px 10px var(--card-shadow);
  }
  .card-front { top: 90px; }
  .card-back { top: 469px; }

  .contact-block {
    position: absolute;
    top: 86px;
    left: 0;
    width: 100%;
    text-align: center;
  }
  .person-name {
    font-weight: 700;
    font-size: 20px;
    letter-spacing: 0.5px;
    line-height: 24px;
  }
  .person-role {
    font-size: 15px;
    line-height: 18px;
  }
  .divider {
    width: 142px;
    height: 1px;
    background: var(--ink);
    margin: 8px auto 0;
  }
  .contact-list {
    list-style: none;
    margin-top: 10px;
    font-size: 15px;
    line-height: 20.5px;
  }
  .contact-list .label { font-weight: 700; }
  .contact-block .divider.lower { margin-top: 10px; }
  .services {
    position: absolute;
    top: 236px;
    left: 0;
    width: 100%;
    text-align: center;
    font-size: 15.5px;
    white-space: nowrap;
  }
  .services .dot {
    display: inline-block;
    width: 7px;
    height: 7px;
    border-radius: 50%;
    background: var(--ink);
    margin: 0 8px;
    vertical-align: middle;
  }

  .brand-mark {
    position: absolute;
    top: 0;
    left: 0;
    width: 100%;
    height: 100%;
    display: flex;
    align-items: center;
    justify-content: center;
    gap: 14px;
  }
  .brand-square {
    width: 22px;
    height: 22px;
    background: var(--ink);
  }
  .brand-name {
    font-weight: 900;
    font-size: 38px;
    letter-spacing: 0.5px;
    color: var(--ink);
  }
</style>
</head>
<body>
<main class="stage">
  <section class="card card-front" aria-label="Business card front">
    <div class="contact-block">
      <h1 class="person-name">DANIEL HARPER</h1>
      <p class="person-role">Quality Manager</p>
      <div class="divider"></div>
      <ul class="contact-list">
        <li><span class="label">P:</span> 555-014-2730</li>
        <li><span class="label">E:</span> dan.Brightwell@mailbox.example</li>
        <li><span class="label">W:</span> www.BrightwellPainting.example</li>
      </ul>
      <div class="divider lower"></div>
    </div>
    <p class="services">Exterior Painting<span class="dot"></span>Interior Painting<span class="dot"></span>Carpentry<span class="dot"></span>Drywall</p>
  </section>

  <section class="card card-back" aria-label="Business card back">
    <div class="brand-mark">
      <span class="brand-square"></span>
      <span class="brand-name">Brightwell Painting</span>
    </div>
  </section>
</main>
</body>
</html>
```